Natural Skincare Product Labels Design

We are looking for a designer to create elegant but quirky, functional product labels for our natural skincare range.
The labels must reflect our brand’s values of simplicity, luxury, and the natural, handmade essence of our products.
https://www.pictogrove.com/marvellaskincare
1. Key Details
Packaging Dimensions
Container Types: Transparent jars.
Sizes for Body Products:
Diameter: 64mm–68mm.
Heights: 80mm, 88mm, and 97mm (lid height: 15mm).
Sizes for Face Creams:
Diameter: 60mm.
Height: 50mm (lid height: 15mm).
Label Fit: For body products, ideally one label size to fit all jar sizes.
For the smaller face cream jars, a separate, tailored label is required.
2. Label Placement
Options include a wrapped-around label or a combination of wrapped-around and top-of-jar elements.
Transparent jars mean the label must leave space for the product to be visible (e.g., partial wrap or cutout areas).
3. Content Requirements
Product Name: Prominently displayed.
Ingredient List: Dedicated space required.
Disclaimer/Usage Instructions: Include space for this information.
4. Design Goals
Look & Feel: Simple, upmarket, and natural, with a handmade essence.
Logo Usage: Our logo is finalized and available in gold, black, and white variants. Use Josefin Bold font for the logo if adjustments are required.
Color Palette: Neutral tones (e.g., whites, blacks, golds) are preferred, with flexibility for subtle pops of color tied to each product’s main ingredient.
5. Imagery
Open to including images and colours (e.g., botanical illustrations) that highlight the main ingredient (e.g., coffee beans, turmeric root, or honeycomb). Also open to labels having a prominent colour to tie it in to the main ingredient.
Alternatively, no images can also work for a clean design.
6. Current Design Context
Our temporary design features gold leaf on top and a simple handmade side label. We’re seeking to elevate this to a more polished, cohesive design.
7. Product Line
- Body Products (Larger Jars)
Tolo Body Butter
Key Ingredients: Guarana & Cupuaçu butter (inspired by Brazil).
Note: “Tolo” is slang for “bum.”
Manuka Honey Body Butter
Key Ingredients: Manuka honey (from New Zealand) & Cupuaçu butter.
Coffee Body Scrub
Key Ingredients: Coffee and Demerara sugar.
Whipped Body Soap - Turmeric
Key Ingredients: Turmeric and Bentonite clay.
Whipped Body Soap - Banana
- Face Products (Smaller Jars)
Face Cream
Key Ingredients: Carrot Oil and Raspberry Oil.
Features natural UV protection.
Good Night Cream
Key Ingredients: Enriched with Magnesium.
Promotes relaxation and restful sleep.
8. Submission Guidelines
Flexibility: Design should allow for consistent branding across all products while accommodating the varying jar sizes and ingredient focus.
Material Considerations: Labels should complement the transparent jars and allow the product inside to remain partially visible.
Print Elements: Incorporating gold accents is a plus but should not overpower the design.
We’re excited to see your vision for a label that celebrates the natural beauty and high quality of our skincare range. Please include mockups to showcase the design in use, particularly on transparent jars of varying sizes.
women 20-50 years of age

```html
<!DOCTYPE html>
<html lang="en">
<head>
<meta charset="utf-8">
<title>Marvella Face Cream Label</title>
<link href="https://fonts.googleapis.com/css2?family=IBM+Plex+Sans:wght@300;400;700&family=Source+Serif+4:opsz,wght@8..60,800&family=Josefin+Sans:wght@700&display=swap" rel="stylesheet">
<style>
  :root {
    --backdrop: #333333;
    --label: #ffffff;
    --accent: #d45c38;
    --gold: #b8902f;
    --ink: #222222;
    --note: #ffffff;
  }
  html, body {
    margin: 0;
    padding: 0;
    width: 1200px;
    height: 1200px;
    overflow: hidden;
    background: var(--backdrop);
    font-family: "IBM Plex Sans", sans-serif;
  }
  .canvas { position: relative; width: 1200px; height: 1200px; }
  .spec-note {
    position: absolute;
    left: 71px;
    top: 74px;
    color: var(--note);
    font-weight: 400;
    font-size: 27px;
    line-height: 32px;
  }
  .label {
    position: absolute;
    left: 59px;
    top: 458px;
    width: 1082px;
    height: 284px;
    background: var(--label);
    border-radius: 31px;
  }
  .brand-seal {
    position: absolute;
    left: 116px;
    top: 542px;
    width: 114px;
    height: 114px;
    border: 1.5px solid var(--gold);
    border-radius: 50%;
    box-sizing: border-box;
    display: flex;
    align-items: center;
    justify-content: center;
  }
  .brand-name {
    font-family: "Josefin Sans", sans-serif;
    font-weight: 700;
    font-size: 17px;
    letter-spacing: 1.5px;
    text-transform: uppercase;
    color: var(--gold);
  }
  .key-oils {
    position: absolute;
    left: 259px;
    top: 532px;
    margin: 0;
    font-size: 25px;
    line-height: 25px;
    font-weight: 400;
    color: var(--accent);
  }
  .product-name {
    position: absolute;
    left: 258px;
    top: 554px;
    margin: 0;
    font-family: "Source Serif 4", serif;
    font-weight: 800;
    font-size: 57px;
    line-height: 57px;
    color: var(--accent);
  }
  .rule-horizontal {
    position: absolute;
    left: 258px;
    top: 628px;
    width: 541px;
    height: 1px;
    background: var(--accent);
  }
  .rule-vertical {
    position: absolute;
    left: 799px;
    top: 514px;
    width: 1px;
    height: 171px;
    background: var(--accent);
  }
  .benefit, .volume {
    position: absolute;
    top: 647px;
    margin: 0;
    font-size: 20px;
    line-height: 20px;
    font-weight: 300;
    color: var(--ink);
  }
  .benefit { left: 257px; }
  .volume { right: calc(1200px - 777px); }
  .info-block { position: absolute; left: 828px; width: 270px; }
  .info-block h2 {
    margin: 0;
    font-size: 17px;
    line-height: 19px;
    font-weight: 700;
    color: var(--accent);
  }
  .info-block p {
    margin: 0;
    font-size: 16px;
    line-height: 19px;
    font-weight: 400;
    color: var(--ink);
  }
  .ingredients { top: 523px; }
  .directions { top: 620px; }
</style>
</head>
<body>
<div class="canvas">
  <div class="spec-note">Label Size<br>95 x 25 mm</div>

  <div class="label"></div>

  <div class="brand-seal"><span class="brand-name">Marvella</span></div>

  <p class="key-oils">Carrot Oil • Raspberry Oil</p>
  <h1 class="product-name">Face Cream</h1>
  <div class="rule-horizontal"></div>
  <p class="benefit">Features natural UV protection</p>
  <p class="volume">50 ml</p>

  <div class="rule-vertical"></div>

  <section class="info-block ingredients">
    <h2>Ingredients</h2>
    <p>Carrot Oil, Raspberry Oil, Shea Butter, Jojoba Oil, Vitamin E, Aloe Vera Extract.</p>
  </section>
  <section class="info-block directions">
    <h2>How to Use</h2>
    <p>Apply to cleansed face every morning.</p>
  </section>
</div>
</body>
</html>
```